Stationary for Green cleaners and green products
Fresh Leaf Laundry n Goods
Stationary for Green cleaners and green products - Retailers
Creative Brief
Use same font as used in my logo
Harold J Benton
President
4730 Maple Row Millbrook, OH 45220
606-514-7720 or 514-7721
1freshleaflaundry@mailbox-example.com
freshleaflaundry-example.org or.net or .biz
logo also being developed at this site
list of services Dry Cleaning Laundry household items, draperies, leather, wedding gowns, full alterations services green friendly products
Concepts
Business Cards/Letterhead/ Envelopes/Notepads/Tshirt/labels for little big box
Business Card for Womens Clothing Boutique

```html
<!DOCTYPE html>
<html lang="en">
<head>
<meta charset="utf-8">
<title>Fresh Leaf Laundry n Goods – Business Card</title>
<link href="https://fonts.googleapis.com/css2?family=Open+Sans:wght@400;600;700&display=swap" rel="stylesheet">
<style>
  :root{
    --backdrop:#e9ece8;
    --card:#ffffff;
    --green-dark:#3f9a1c;
    --green:#5cb82a;
    --green-light:#9fd65e;
    --green-pale:#c6e79a;
    --ink:#3b3b3b;
    --on-band:#ffffff;
  }
  *{box-sizing:border-box;margin:0;padding:0}
  html,body{width:1200px;height:914px;overflow:hidden;background:var(--backdrop)}
  body{font-family:"Open Sans",Arial,sans-serif;color:var(--ink)}
  .business-card{
    position:absolute;left:100px;top:171px;width:1000px;height:572px;
    background:var(--card);box-shadow:0 6px 24px rgba(0,0,0,.12);
  }
  .brand{
    position:absolute;top:62px;left:0;right:0;
    display:flex;flex-direction:column;align-items:center;gap:18px;
  }
  .brand-dot{width:76px;height:76px;border-radius:50%;background:var(--green)}
  .brand-name{font-weight:700;font-size:40px;color:var(--green-dark);letter-spacing:.2px}
  .title-band{
    position:absolute;left:0;right:0;top:278px;height:78px;
    background:linear-gradient(90deg,var(--green-light) 0%,var(--green) 35%,var(--green-dark) 100%);
  }
  .title-strip{
    position:absolute;left:0;right:0;bottom:0;height:32px;
    background:linear-gradient(90deg,var(--green-pale),var(--green-light) 60%,var(--green));
    display:flex;align-items:center;justify-content:center;
    font-size:17px;font-weight:600;color:var(--on-band);
  }
  .title-strip .role{font-weight:400;margin-left:8px}
  .band-rule{position:absolute;left:0;right:0;top:366px;height:3px;background:var(--green)}
  .contacts{
    position:absolute;left:34px;right:34px;top:396px;
    display:flex;flex-direction:column;gap:16px;font-size:16px;
  }
  .contact-row{display:flex;gap:22px;align-items:center;flex-wrap:nowrap}
  .contact-row.second{padding-left:150px}
  .contact{display:flex;align-items:center;gap:7px;white-space:nowrap}
  .contact svg{width:20px;height:20px;flex:none}
  .foot-rule{position:absolute;left:0;right:0;bottom:22px;height:8px;background:var(--green)}
</style>
</head>
<body>
<div class="business-card">
  <div class="brand">
    <div class="brand-dot"></div>
    <div class="brand-name">Fresh Leaf Laundry n Goods</div>
  </div>

  <div class="title-band">
    <div class="title-strip">Harold J Benton <span class="role">/ President</span></div>
  </div>
  <div class="band-rule"></div>

  <div class="contacts">
    <div class="contact-row">
      <span class="contact"><svg viewBox="0 0 20 20"><circle cx="10" cy="10" r="10" fill="#5cb82a"/><path d="M7 5l2 3-1 1a6 6 0 003 3l1-1 3 2-1 2c-4 0-9-5-9-9z" fill="#fff"/></svg>606-514-7720</span>
      <span class="contact"><svg viewBox="0 0 20 20"><circle cx="10" cy="10" r="10" fill="#5cb82a"/><path d="M7 5l2 3-1 1a6 6 0 003 3l1-1 3 2-1 2c-4 0-9-5-9-9z" fill="#fff"/></svg>606-514-7721</span>
      <span class="contact"><svg viewBox="0 0 20 20"><circle cx="10" cy="10" r="10" fill="#5cb82a"/><path d="M7 5l2 3-1 1a6 6 0 003 3l1-1 3 2-1 2c-4 0-9-5-9-9z" fill="#fff"/></svg>606-518-2290</span>
      <span class="contact"><svg viewBox="0 0 20 20"><circle cx="10" cy="10" r="10" fill="#5cb82a"/><path d="M7 5l2 3-1 1a6 6 0 003 3l1-1 3 2-1 2c-4 0-9-5-9-9z" fill="#fff"/></svg>606-517-3345</span>
      <span class="contact"><svg viewBox="0 0 20 20"><circle cx="10" cy="10" r="10" fill="#5cb82a"/><circle cx="10" cy="10" r="5.5" fill="none" stroke="#fff" stroke-width="1.3"/><path d="M4.5 10h11M10 4.5c-3 3-3 8 0 11M10 4.5c3 3 3 8 0 11" fill="none" stroke="#fff" stroke-width="1.1"/></svg>www.freshleaflaundry-example.org</span>
    </div>
    <div class="contact-row second">
      <span class="contact"><svg viewBox="0 0 20 20"><circle cx="10" cy="10" r="10" fill="#5cb82a"/><path d="M10 4a4 4 0 014 4c0 3-4 8-4 8s-4-5-4-8a4 4 0 014-4z" fill="#fff"/><circle cx="10" cy="8" r="1.5" fill="#5cb82a"/></svg>4730 Maple Row Millbrook, OH 45220</span>
      <span class="contact"><svg viewBox="0 0 20 20"><circle cx="10" cy="10" r="10" fill="#5cb82a"/><rect x="5" y="6.5" width="10" height="7" fill="#fff"/><path d="M5 6.5l5 4 5-4" fill="none" stroke="#5cb82a" stroke-width="1"/></svg>1freshleaflaundry@mailbox-example.com</span>
    </div>
  </div>

  <div class="foot-rule"></div>
</div>
</body>
</html>
```